Banner Ads for Online Poker Promotion

We are an online poker network, the QLT (www.theqlt.eu). We are looking for a small selection of web banner ads for our latest promotion.

Banner sizes that we need are:
- 196x523 (static .psd and .png)
- 199x129 (static .psd and .png)
- 447x426 (static .psd and .png)
- 500x400 (static .psd and .png)
- 697x167 (static .psd and .png)
- 460x60 (animated .gif)

The promotion name is ‘Drop & Play Plunder’ (or ‘DNP Plunder’) and the concept is that certain Sit & Go tournaments have money added to the prize pool. Basically, free cash for Sit & Go players.

(If you don’t know poker, a ‘Sit & Go’ is a tournament which starts when a specific number of players join, as opposed to a scheduled tournament which starts at a specific time).

The promotion starts on November 3rd.

Guidelines:

The name of the promotion, ‘Drop & Play Plunder’ or ‘DNP Plunder’, should feature prominently in the banners.

The strap line can be ‘Get Your Share of the Loot’, ‘Added Money in SNGs’ or something similar (feel free to be creative).

Our network logo (attached) must feature on the animated .gif. It is optional on the other banners.

Examples of past promotional imagery can be found on our website, in particular these pages: http://www.theqlt.eu/promotions/ and http://www.theqlt.eu/promotions/archived-promotions/ . Our last promotion was crowdsourced and the details of that and the winner can be found here: http://jobs.artvolley.com/job.aspx?id=514372

We are looking to go in a more modern and risqué direction than the past, in order to stand out from competition which is very bland.

Common poker imagery –cards, chips, suit icons etc – or objects associated with live poker (tables, etc) is a little clichéd. It can be included if it has a clear purpose. But don’t just put flying cards or suit symbols in there for no reason.

More like iOS7/8, less like iOS6

Think flat, modern, glamour, clean, fresh, bright, rock music, extreme sports, and the Iron Thunder!

Most of our customers are 18-35, male, and we have a strong European focus.

As we are a gaming company, the banners must not encourage underage play, problem gambling, or associate gambling with sexual or social success.

If any further guidance is needed please don’t hesitate to ask!

```html
<!DOCTYPE html>
<html lang="en">
<head>
<meta charset="utf-8">
<title>DNP Plunder – Get Your Share of the Loot!</title>
<link rel="stylesheet" href="https://fonts.googleapis.com/css2?family=Graduate&family=Archivo+Black&family=Roboto:wght@700&display=swap">
<style>
  :root {
    --red-bright: #ff2a2a;
    --red-mid: #e0121a;
    --red-deep: #a8060c;
    --red-dark: #6e0307;
    --white: #ffffff;
    --ink: #2a0000;
    --title-stroke: #d0101a;
  }
  html, body {
    margin: 0;
    padding: 0;
    width: 1200px;
    height: 288px;
    overflow: hidden;
    background: var(--red-mid);
  }
  .banner {
    position: relative;
    width: 1200px;
    height: 288px;
    overflow: hidden;
    background: radial-gradient(ellipse 70% 120% at 52% 45%, var(--red-bright) 0%, var(--red-mid) 45%, var(--red-deep) 100%);
    font-family: "Roboto", sans-serif;
  }
  .banner__rays {
    position: absolute;
    inset: 0;
    width: 100%;
    height: 100%;
  }
  .banner__compass {
    position: absolute;
    left: 450px;
    top: -60px;
    width: 360px;
    height: 360px;
    border-radius: 50%;
    background: radial-gradient(circle, rgba(150, 0, 8, 0.55) 0%, rgba(170, 4, 12, 0.35) 45%, rgba(200, 10, 20, 0) 70%);
  }
  .brand {
    position: absolute;
    left: 16px;
    top: 22px;
    display: flex;
    flex-direction: column;
    align-items: center;
    gap: 6px;
  }
  .brand__dot {
    width: 22px;
    height: 22px;
    border-radius: 50%;
    background: var(--white);
  }
  .brand__name {
    font-family: "Roboto", sans-serif;
    font-weight: 700;
    font-size: 26px;
    color: var(--white);
    line-height: 1;
  }
  .date {
    position: absolute;
    right: 18px;
    top: 20px;
    margin: 0;
    font-family: "Roboto", sans-serif;
    font-weight: 700;
    font-size: 24px;
    color: var(--white);
  }
  .title {
    position: absolute;
    left: 615px;
    top: 50px;
    transform: translateX(-50%);
    margin: 0;
    white-space: nowrap;
    font-family: "Graduate", serif;
    font-weight: 400;
    font-size: 112px;
    line-height: 1.2;
    letter-spacing: 4px;
    color: var(--white);
    -webkit-text-stroke: 3px var(--title-stroke);
    paint-order: stroke fill;
    text-shadow:
      0 0 0 var(--white),
      3px 3px 0 var(--white),
      5px 5px 0 var(--ink),
      6px 7px 6px rgba(0, 0, 0, 0.45);
  }
  .strapline {
    position: absolute;
    left: 620px;
    top: 196px;
    transform: translateX(-50%);
    margin: 0;
    white-space: nowrap;
    font-family: "Archivo Black", sans-serif;
    font-size: 44px;
    font-style: italic;
    letter-spacing: 2px;
    color: var(--white);
    text-shadow:
      2px 2px 0 var(--ink),
      3px 4px 0 var(--red-dark),
      0 0 6px rgba(0, 0, 0, 0.5);
  }
</style>
</head>
<body>
  <main class="banner">
    <svg class="banner__rays" viewBox="0 0 1200 288" preserveAspectRatio="none" aria-hidden="true">
      <g fill="#ff4a4a" opacity="0.25">
        <polygon points="620,144 0,0 160,0"/>
        <polygon points="620,144 330,0 470,0"/>
        <polygon points="620,144 760,0 900,0"/>
        <polygon points="620,144 1060,0 1200,0"/>
        <polygon points="620,144 1200,110 1200,220"/>
        <polygon points="620,144 1080,288 940,288"/>
        <polygon points="620,144 700,288 560,288"/>
        <polygon points="620,144 330,288 190,288"/>
        <polygon points="620,144 0,200 0,288"/>
        <polygon points="620,144 0,70 0,130"/>
      </g>
    </svg>
    <div class="banner__compass" role="img" aria-label="Large faint compass star decoration behind the title"></div>

    <div class="brand">
      <span class="brand__dot" aria-hidden="true"></span>
      <span class="brand__name">QLT</span>
    </div>

    <p class="date">November 3rd</p>

    <h1 class="title">DNP PLUNDER</h1>
    <p class="strapline">Get Your Share of the Loot!</p>
  </main>
</body>
</html>
```